Valmora Building Company Portfolio Design

I need a full design for a Company Portfolio for a Kuwait based company called Valmora Building Company, WLL. We offer services in Construction ( Supply of Construction Machinery & Construction Material), Contracting (Steel Structure, Furnishing & Finishing) and Smart Solutions (Smart Homes & Smart Parking).

https://www.filetarn.example/s/qpzk4vn82tmhdwe/Photos.zip

This is a File Tarn Link containing all our images that can be used in the Company Profile.

One or more of each can be more than enough to describe each product or service we provide.

Target Market(s)

Construction Companies, Engineering & Design Companies, Consultancy firms.

Industry/Entity Type

Construction

Requirements
Must have
• 1) Must allow for further addition & modification.
Nice to have
• 1) External Photos can be used for a better look & resolution.

```html
<!DOCTYPE html>
<html lang="en">
<head>
<meta charset="utf-8">
<title>Valmora Building Company – Our Mission</title>
<link href="https://fonts.googleapis.com/css2?family=Carlito:wght@400;700&family=Open+Sans:wght@700;800&family=Cairo:wght@600&display=swap" rel="stylesheet">
<style>
  :root {
    --teal: #0b7b80;
    --teal-deep: #06585c;
    --black: #000000;
    --white: #ffffff;
    --sky-light: #9fb4d6;
    --sky-mid: #4f6fae;
    --sky-deep: #24408a;
    --tower: #c9d3e2;
    --ink: #1a1a1a;
  }
  * { margin: 0; padding: 0; box-sizing: border-box; }
  html, body { width: 1200px; height: 901px; overflow: hidden; background: var(--white); }
  .page { position: relative; width: 1200px; height: 901px; background: var(--white); overflow: hidden; }

  /* upper spread */
  .side-band { position: absolute; background: var(--teal); }
  .side-band--edge { left: 0; top: 0; width: 7px; height: 623px; }
  .side-band--main { left: 15px; top: 0; width: 153px; height: 623px; }
  .side-black { position: absolute; left: 1046px; top: 0; width: 154px; height: 623px; background: var(--black); }

  .mission-panel {
    position: absolute; left: 168px; top: 4px; width: 878px; height: 616px;
    background:
      radial-gradient(ellipse 45% 70% at 55% 55%, var(--tower) 0%, rgba(201,211,226,0.35) 45%, transparent 75%),
      linear-gradient(180deg, var(--sky-deep) 0%, var(--sky-mid) 45%, var(--sky-light) 100%);
    border-bottom: 4px solid var(--ink);
  }

  .brand { position: absolute; color: var(--ink); }
  .brand--latin {
    left: 62px; top: 28px;
    font-family: "Carlito", sans-serif; font-weight: 700;
    font-size: 30px; letter-spacing: 3px; line-height: 1;
  }
  .brand--latin small { display: block; font-size: 11px; letter-spacing: 3.5px; margin-top: 4px; }
  .brand--mark { left: 408px; top: 38px; width: 22px; height: 22px; background: var(--teal); }
  .brand--arabic {
    right: 58px; top: 28px; direction: rtl; text-align: right;
    font-family: "Cairo", sans-serif; font-weight: 600; font-size: 24px; line-height: 1.2;
  }

  .mission-title {
    position: absolute; left: 0; width: 100%; top: 162px; text-align: center;
    font-family: "Open Sans", sans-serif; font-weight: 800; font-size: 34px;
    letter-spacing: 9px; color: var(--white);
    text-shadow: 2px 2px 2px var(--ink);
  }
  .mission-text {
    position: absolute; left: 47px; top: 250px; width: 800px;
    font-family: "Carlito", sans-serif; font-size: 24.5px; line-height: 32.5px;
    color: var(--white);
    text-shadow: 1.5px 1.5px 1.5px var(--ink);
  }

  /* lower spread */
  .divider { position: absolute; left: 0; top: 623px; width: 1200px; height: 7px; background: var(--white); }
  .lower-band {
    position: absolute; left: 0; top: 630px; width: 1200px; height: 271px;
    background: linear-gradient(90deg, var(--teal) 0%, var(--teal) 18%, var(--teal-deep) 28%, #02191b 36%, var(--black) 40%, var(--black) 100%);
  }
  .lower-rule { position: absolute; left: 7px; top: 630px; width: 8px; height: 271px; background: var(--white); }
  .tech-visual {
    position: absolute; left: 440px; top: 630px; width: 560px; height: 271px;
    background:
      radial-gradient(ellipse 30% 25% at 62% 88%, rgba(255,240,190,0.75) 0%, rgba(255,210,120,0.25) 45%, transparent 80%),
      radial-gradient(ellipse 55% 60% at 45% 40%, rgba(170,200,230,0.45) 0%, rgba(40,70,110,0.3) 55%, transparent 85%),
      radial-gradient(ellipse 60% 70% at 50% 55%, #13233a 0%, transparent 80%);
  }
</style>
</head>
<body>
<main class="page">
  <div class="side-band side-band--edge"></div>
  <div class="side-band side-band--main"></div>
  <div class="side-black"></div>

  <section class="mission-panel" role="img" aria-label="Photograph of curving glass high-rise towers against a blue sky">
    <div class="brand brand--latin">VALMORA<small>BUILDING COMPANY</small></div>
    <div class="brand brand--mark"></div>
    <div class="brand brand--arabic">فالمورا للإنشاءات العامة</div>

    <h1 class="mission-title">OUR MISSION</h1>
    <p class="mission-text">Our mission is to supply our customers with the highest level of quality construction services at fair and market competitive prices and to ensure the longevity of our company through repeat and referral clients achieved by customer satisfaction in all areas including timelines, attention to detail and service-minded attitudes. We are to maintain the highest levels of professionalism, integrity, honesty and fairness in our relationships with our suppliers, subcontractors, professional associates and customers</p>
  </section>

  <div class="divider"></div>
  <div class="lower-band"></div>
  <div class="lower-rule"></div>
  <div class="tech-visual" role="img" aria-label="Photograph of hands holding a tablet projecting glowing wireframe building models"></div>
</main>
</body>
</html>
```